Tincture Design for Woman Owned CBD Branf

LumiVelle is a luxery CBD brand for millennial women.

Our premium L Oil contains 500mg of full spectrum CBD derived from specially-sourced hemp for unparalleled purity and quality. Each dropper delivers approximately 20mg of CBD. Available in two flavors, Natural and Mint.

The goal is to design an aesthetically pleasing tincture (bottle dropper) with label and box. The final design should coincide with our brand guidelines and easily marketed for beauty consumers. We are looking for a clean design, the use of raised fonts and/or metallic is fine.

We have 4 other designs we'd like to work on with the winning designer.

Target Market(s)

Millennial Women, Income $75k+

Font styles to use
Other font styles liked:
• See Branding Sheet

Requirements
Must have
• Must follow brand guidelines (see attached for colors, font, etc)
Nice to have
• Raised font or Metallic Print

```html
<!DOCTYPE html>
<html lang="en">
<head>
<meta charset="utf-8">
<title>LumiVelle Premium L Oil – Label and Box</title>
<link rel="stylesheet" href="https://fonts.googleapis.com/css2?family=Cormorant+Garamond:wght@400;500;600&family=Montserrat:wght@400;600;800&display=swap">
<style>
  :root {
    --bg: #e9ebee;
    --blush: #e3bfb6;
    --blush-deep: #dcab9f;
    --label-pink: #e0ab97;
    --rust: #b35a3d;
    --rust-band: #b96c4c;
    --green: #0f5a4a;
    --gold: #c49253;
    --white: #f6f6f5;
    --cream: #ffffff;
  }
  * { margin: 0; padding: 0; box-sizing: border-box; }
  html, body { width: 1200px; height: 1198px; overflow: hidden; }
  body { background: var(--bg); position: relative; font-family: "Cormorant Garamond", serif; }

  /* ---------- Bottle label ---------- */
  .label {
    position: absolute; left: 250px; top: 560px; width: 300px; height: 390px;
    background: var(--label-pink); overflow: hidden;
  }
  .label-top {
    position: absolute; left: 0; top: 0; width: 100%; height: 170px;
    background: var(--cream); border-bottom-left-radius: 50% 40px; border-bottom-right-radius: 50% 40px;
  }
  .label-seal {
    position: absolute; left: 42px; top: 12px; width: 216px; height: 150px;
    border: 1.5px solid var(--blush-deep); border-radius: 50%; background: var(--cream);
    text-align: center;
  }
  .seal-est { font-family: "Montserrat", sans-serif; font-size: 8px; letter-spacing: 5px; color: var(--gold); margin-top: 16px; }
  .seal-name { font-size: 40px; line-height: 38px; color: var(--green); margin-top: 10px; letter-spacing: 2px; }
  .seal-tag { font-family: "Montserrat", sans-serif; font-size: 7px; letter-spacing: 4px; color: var(--gold); margin-top: 10px; }
  .label-title { position: absolute; top: 178px; width: 100%; text-align: center; font-size: 33px; font-weight: 600; color: var(--rust); }
  .label-dose { position: absolute; top: 200px; width: 100%; text-align: center; font-size: 96px; font-weight: 600; color: var(--rust); line-height: 96px; letter-spacing: -2px; }
  .label-band {
    position: absolute; left: 30px; top: 292px; width: 240px; height: 44px; background: var(--rust-band);
    color: var(--label-pink); text-align: center; font-size: 19px; line-height: 19px; padding-top: 3px;
  }
  .label-foot { position: absolute; top: 350px; left: 0; width: 100%; display: flex; justify-content: space-around; align-items: center;
    font-family: "Montserrat", sans-serif; font-size: 10px; color: var(--rust); text-align: center; line-height: 12px; }
  .label-badge { width: 34px; height: 34px; border-radius: 50%; border: 1.5px solid var(--rust); }

  /* ---------- Box front ---------- */
  .box { position: absolute; left: 690px; top: 190px; width: 300px; height: 812px; background: var(--white); }
  .box-head { position: absolute; top: 0; left: 0; width: 100%; height: 250px; background: var(--blush); text-align: center; }
  .head-est { font-family: "Montserrat", sans-serif; font-size: 8px; letter-spacing: 5px; color: var(--cream); margin-top: 88px; }
  .head-name { font-size: 50px; letter-spacing: 3px; color: var(--cream); margin-top: 30px; line-height: 50px; }
  .head-tag { font-family: "Montserrat", sans-serif; font-size: 7px; font-weight: 600; letter-spacing: 4px; color: var(--gold); margin-top: 10px; }
  .box-monogram { position: absolute; left: 20px; top: 305px; width: 80px; height: 170px; background: linear-gradient(180deg, #d7e4df, #eef2f0); }
  .box-strength { position: absolute; right: 26px; top: 312px; text-align: right; font-family: "Montserrat", sans-serif; font-weight: 800; color: var(--blush-deep); }
  .strength-kind { font-size: 23px; }
  .strength-value { font-size: 64px; line-height: 64px; }
  .strength-unit { font-size: 28px; line-height: 30px; }
  .box-claim { position: absolute; left: 38px; top: 522px; width: 224px; height: 62px; border-top: 3px solid var(--blush-deep); border-bottom: 3px solid var(--blush-deep);
    text-align: center; color: var(--rust); font-size: 19px; line-height: 19px; padding-top: 10px; }
  .box-badge { position: absolute; left: 104px; top: 618px; width: 92px; height: 92px; border-radius: 50%; background: var(--blush); border: 3px solid var(--blush-deep); }
  .box-foot { position: absolute; bottom: 0; left: 0; width: 100%; height: 90px; background: var(--blush); text-align: center;
    font-family: "Montserrat", sans-serif; font-size: 12px; color: var(--cream); line-height: 22px; padding-top: 24px; letter-spacing: 0.5px; }
</style>
</head>
<body>
  <section class="label" aria-label="Bottle label">
    <div class="label-top">
      <div class="label-seal">
        <p class="seal-est">EST. 2020</p>
        <p class="seal-name">LUMI<br>VELLE</p>
        <p class="seal-tag">PREMIUM CBD</p>
      </div>
    </div>
    <p class="label-title">Premium L Oil</p>
    <p class="label-dose">500mg</p>
    <p class="label-band">CBD derived from<br>specially-sourced hemp</p>
    <div class="label-foot">
      <span>NATURAL<br>FLAVOR</span>
      <span class="label-badge"></span>
      <span>1 oz/30 ml</span>
    </div>
  </section>

  <section class="box" aria-label="Box front">
    <div class="box-head">
      <p class="head-est">EST. 2020</p>
      <p class="head-name">LUMIVELLE</p>
      <p class="head-tag">PREMIUM CBD PRODUCTS</p>
    </div>
    <div class="box-monogram" role="img" aria-label="Decorative brand initial area"></div>
    <div class="box-strength">
      <p class="strength-kind">PREMIUM OIL</p>
      <p class="strength-value">500</p>
      <p class="strength-unit">MG</p>
    </div>
    <p class="box-claim">CBD derived from<br>specially-sourced hemp</p>
    <div class="box-badge"></div>
    <div class="box-foot">NATURAL FLAVOR<br>1 oz/30 ml</div>
  </section>
</body>
</html>
```